refurbishment of diamond cut alloy wheels

we need to design a flyer that will catch the eye of the customer to refurbish diamond cut alloy wheels. we refurbish the wheels by using the latest CNC machine to precision cut and resurface the wheel. we would like before and after pictures of maybe Kelvaron, DXT, Orsa wheels to give it a prestige look. The final design should communicate an expensive look and providing a good image for the business. The colours that I would like to use is black and red which should make the flyer stand out. The logo must sit on a black background without the wordings of specialists in HJ, Orsa etc and also without servicing, diagnostics etc as well. This flyer is just to communicate refurbishment of alloy wheels to high standard.

Target Market(s)

any members of the public and car dealerships

Industry/Entity Type

Automotive

Colors

Designer to choose colors to be used in the design.

Requirements
Must have
• Wow factor with great images of wheels
Nice to have
• Maybe on the front of the flyer it has a picture of a wheel and then on the back of the flyer it has before and after pictures to show how just how incredible it is to refurbish wheels
Should not have
• other makes of wheels apart from DXT, Orsa, and any other high end makes of vehicles wheels

```html
<!DOCTYPE html>
<html lang="en">
<head>
<meta charset="utf-8">
<title>Tallis Motors – Wheels &amp; Refurbishments Flyer</title>
<link href="https://fonts.googleapis.com/css2?family=Archivo+Black&family=Fira+Sans:wght@300;400;500&family=Josefin+Sans:wght@400;600&family=Tenor+Sans&display=swap" rel="stylesheet">
<style>
:root{
  --bg:#3a3a3c;
  --black:#0d0d0f;
  --red:#8b1c1f;
  --red-bright:#c0262b;
  --grey-dark:#2a2b2e;
  --grey:#4a4b4f;
  --white:#ffffff;
  --text-soft:#e4e4e4;
}
*{margin:0;padding:0;box-sizing:border-box}
html,body{width:1200px;height:863px;overflow:hidden;background:var(--bg)}
.stage{position:relative;width:1200px;height:863px}
.flyer{position:absolute;top:41px;width:552px;height:780px;overflow:hidden;background:var(--grey-dark);font-family:"Fira Sans",sans-serif;color:var(--white)}
.flyer--back{left:32px}
.flyer--front{left:616px;background:var(--black)}
.abs{position:absolute}

/* brand mark */
.brand{display:flex;align-items:center;gap:8px}
.brand__dot{width:13px;height:13px;background:var(--red-bright)}
.brand__name{font-family:"Archivo Black",sans-serif;font-size:19px;color:var(--white);letter-spacing:.5px;line-height:1;white-space:nowrap}
.back-header .brand__name{font-size:15px}
.back-header .brand__dot{width:11px;height:11px}

/* back flyer */
.back-header{left:0;top:0;width:200px;height:132px;background:var(--black);display:flex;align-items:center;justify-content:center}
.title-box{left:200px;top:0;width:352px;height:132px;background:var(--red);padding:26px 0 0 18px}
.title-box__main{font-family:"Archivo Black",sans-serif;font-size:44px;line-height:1}
.title-box__sub{font-family:"Archivo Black",sans-serif;font-size:25px;line-height:1.2;margin-top:6px}
.photo{position:absolute}
.photo--before{left:0;top:132px;width:240px;height:240px;background:linear-gradient(135deg,#c23a3c,#7a1d20 45%,#6e6e6e 70%,#9a9a9a)}
.photo--after{left:240px;top:132px;width:312px;height:232px;background:linear-gradient(135deg,#b8202a,#5e1014 40%,#2c2c2e 65%,#8e8e90)}
.photo-label{position:absolute;font-family:"Fira Sans",sans-serif;font-weight:500;font-size:24px}
.photo-label--before{left:22px;top:330px}
.photo-label--after{left:256px;top:320px}
.back-body{left:26px;top:396px;width:500px}
.intro{font-size:11.5px;text-transform:uppercase;line-height:1.6;letter-spacing:.3px}
.intro__phone{color:var(--red-bright)}
.section-heading{font-size:18px;font-weight:500;margin:10px 0 8px}
.body-copy{font-size:8.6px;line-height:1.45;color:var(--text-soft);margin-bottom:8px;font-weight:300}
.cta{font-size:18px;font-weight:500;line-height:1.25;margin-top:22px}

/* footer */
.footer{left:0;top:716px;width:552px;height:64px;background:var(--red);font-family:"Josefin Sans",sans-serif;font-size:8.5px;text-transform:uppercase;letter-spacing:.4px;line-height:1.5}
.footer__item{position:absolute;display:flex;gap:7px;align-items:flex-start}
.footer__item svg{flex:none;margin-top:1px}
.footer__address{left:18px;top:20px}
.footer__phones{left:212px;top:16px}
.footer__email{right:20px;top:16px}

/* front flyer */
.hero-photo{left:0;top:70px;width:552px;height:320px;background:radial-gradient(circle at 50% 55%,#5a5d63 0,#2b2d31 40%,#101113 80%)}
.front-top{left:0;top:0;width:552px;height:110px}
.front-brand{left:0;top:34px;width:552px;display:flex;justify-content:center}
.hero-title{left:0;top:150px;width:552px;text-align:center;font-family:"Tenor Sans",sans-serif;line-height:1}
.hero-title__main{font-size:56px;letter-spacing:2px}
.hero-title__sub{font-size:33px;letter-spacing:1px;margin-top:6px}
.grey-panel{left:0;top:300px;width:552px;height:416px}
.inset-photo{left:190px;top:282px;width:172px;height:100px;border:4px solid var(--red);background:linear-gradient(160deg,#b9bcc1,#6b6e74 45%,#1b1c1f 70%,#8a7a62)}
.columns{left:22px;top:398px;width:508px;display:flex;gap:18px}
.column{flex:1}
.column + .column{border-left:1px solid #6b6c70;padding-left:14px}
.column__heading{font-family:"Archivo Black",sans-serif;font-size:13.5px;margin-bottom:8px}
.column__copy{font-size:8.3px;line-height:1.45;font-weight:300;color:var(--text-soft)}
.quote{left:30px;top:520px;width:495px;font-size:19px;line-height:1.4;font-weight:300}
</style>
</head>
<body>
<div class="stage">

  <!-- back side: before / after -->
  <section class="flyer flyer--back">
    <div class="abs back-header">
      <div class="brand"><span class="brand__dot"></span><span class="brand__name">TALLIS MOTORS</span></div>
    </div>
    <div class="abs title-box">
      <div class="title-box__main">Wheels &amp;</div>
      <div class="title-box__sub">Refurbishments</div>
    </div>

    <div class="photo photo--before" role="img" aria-label="Red car front wheel with a worn diamond cut alloy before refurbishment"></div>
    <div class="photo photo--after" role="img" aria-label="Red car with a freshly refurbished diamond cut five-spoke alloy wheel"></div>
    <div class="photo-label photo-label--before">Before</div>
    <div class="photo-label photo-label--after">After</div>

    <div class="abs back-body">
      <p class="intro">We now offer diamond cut alloy wheel refurbishments.<br>If your alloys need refurbishment<br>contact us today on <span class="intro__phone">01753 555 214</span></p>
      <h2 class="section-heading">Alloy Refurbishment Specialists in and around Slough</h2>
      <p class="body-copy">If you are looking to refresh the look of your car but don't want the expense of new alloys, why not have your existing diamond cut wheels restored? We use the latest CNC machine to precision cut and resurface every wheel to a factory-fresh, mirror-bright finish.</p>
      <p class="body-copy">Kerbed, corroded or lacquer-lifted alloys are stripped, repaired, painted and CNC diamond cut, then sealed with a clear protective coat. At Prime Wheels &amp; Tyres, we refurbish prestige wheels from Kelvaron, DXT and Orsa to the highest standard for private owners and car dealerships alike.</p>
      <p class="cta">If you need premier Alloy Refurbishment services in Slough,<br>please contact us:</p>
    </div>

    <footer class="abs footer">
      <div class="footer__item footer__address">
        <svg width="8" height="11" viewBox="0 0 8 11"><path d="M4 0a4 4 0 0 0-4 4c0 3 4 7 4 7s4-4 4-7a4 4 0 0 0-4-4zm0 5.5A1.5 1.5 0 1 1 4 2.5a1.5 1.5 0 0 1 0 3z" fill="#fff"/></svg>
        <span>14B Larkfield Lane, Colnbrook,<br>Slough, Berkshire, SL3 7QT</span>
      </div>
      <div class="footer__item footer__phones">
        <svg width="9" height="9" viewBox="0 0 10 10"><path d="M2 0l2 2.5-1.2 1.2a6 6 0 0 0 3.5 3.5L7.5 6 10 8l-1.5 2C4 10 0 6 0 1.5z" fill="#fff"/></svg>
        <span>01753 555 214<br>07700 900 318</span>
      </div>
      <div class="footer__item footer__email"><span>info@tallismotors.co.uk</span></div>
    </footer>
  </section>

  <!-- front side: hero wheel -->
  <section class="flyer flyer--front">
    <div class="abs hero-photo" role="img" aria-label="Dark close-up of a multi-spoke diamond cut alloy wheel"></div>
    <svg class="abs front-top" width="552" height="110" viewBox="0 0 552 110" aria-hidden="true">
      <path d="M0 0H552V58Q276 110 0 58Z" fill="#0d0d0f"/>
      <path d="M40 84Q276 108 512 50Q276 98 40 84Z" fill="#c0262b"/>
    </svg>
    <div class="abs front-brand">
      <div class="brand"><span class="brand__dot"></span><span class="brand__name">TALLIS MOTORS</span></div>
    </div>
    <div class="abs hero-title">
      <div class="hero-title__main">WHEELS &amp;</div>
      <div class="hero-title__sub">REFURBISHMENTS</div>
    </div>

    <svg class="abs grey-panel" width="552" height="416" viewBox="0 0 552 416" aria-hidden="true">
      <defs>
        <linearGradient id="panelShade" x1="0" y1="0" x2="0" y2="1">
          <stop offset="0" stop-color="#55565b"/>
          <stop offset="1" stop-color="#3a3b3f"/>
        </linearGradient>
      </defs>
      <path d="M0 80Q276 -10 552 60V416H0Z" fill="#8b1c1f"/>
      <path d="M0 86Q276 0 552 66V416H0Z" fill="url(#panelShade)"/>
    </svg>
    <div class="abs inset-photo" role="img" aria-label="Silver car with a polished diamond cut alloy wheel"></div>

    <div class="abs columns">
      <div class="column">
        <h3 class="column__heading">CNC diamond cutting</h3>
        <p class="column__copy">Tallis Motors restores diamond cut alloy wheels in Slough using the latest CNC machine to precision cut and resurface each wheel, bringing back the sharp, mirror-bright finish your car left the factory with, for private owners and dealerships.</p>
      </div>
      <div class="column">
        <h3 class="column__heading">Committed to quality</h3>
        <p class="column__copy">Ravi Mander is a chief master technician for Orsa, HJ, Novel, Vesk and Kelvaron cars and also the proud owner of Tallis Motors. With over 20 years of experience in the industry, you can be assured that your wheels will receive the high-quality care they deserve.</p>
      </div>
    </div>

    <p class="abs quote">“Brilliant professional knowledgeable technicians delivering excellence at every turn. Hands down the best car, van SUV doctor repair garage in London and the home counties. A hidden gem.”</p>

    <footer class="abs footer">
      <div class="footer__item footer__address">
        <svg width="8" height="11" viewBox="0 0 8 11"><path d="M4 0a4 4 0 0 0-4 4c0 3 4 7 4 7s4-4 4-7a4 4 0 0 0-4-4zm0 5.5A1.5 1.5 0 1 1 4 2.5a1.5 1.5 0 0 1 0 3z" fill="#fff"/></svg>
        <span>14B Larkfield Lane, Colnbrook,<br>Slough, Berkshire, SL3 7QT</span>
      </div>
      <div class="footer__item footer__phones">
        <svg width="9" height="9" viewBox="0 0 10 10"><path d="M2 0l2 2.5-1.2 1.2a6 6 0 0 0 3.5 3.5L7.5 6 10 8l-1.5 2C4 10 0 6 0 1.5z" fill="#fff"/></svg>
        <span>01753 555 214<br>07700 900 318</span>
      </div>
      <div class="footer__item footer__email"><span>info@tallismotors.co.uk</span></div>
    </footer>
  </section>

</div>
</body>
</html>
```